"Coastline Motor Traders" business that imports classic cars, motorbikes and boats from the USA needs a bus

We need a business card design for our new company based in Brisbane Australia called "Coastline Motor Traders". You designed our company logo which I have attached. We source and import American Classic, Muscle and Vintage cars for customers in Australia. We also do the same for motor bikes and we will eventually move into boats. The logo is a very strong one so we feel that the colours of the card can not detract from the logo but enhance it. The font needs to be professional but not boring. We are finding dream machines for people so it needs to feel strong and safe, yet fun and be very cool.

Industry/Entity Type

Business

Contact Information for Business Card

Martin Kelloway

Brisbane, QLD
Australia
Mobile: +61417 562 304
Email: martin kelloway@mailbox-example.com

Requirements
Must have
• Strong logo presence
• Identify what we do
Should not have
• don't want it to be cluttered with text

```html
<!DOCTYPE html>
<html lang="en">
<head>
<meta charset="utf-8">
<title>Coastline Motor Traders – Business Card</title>
<link href="https://fonts.googleapis.com/css2?family=Open+Sans:wght@400;700;800&display=swap" rel="stylesheet">
<style>
  :root {
    --page-bg: #e9e6e1;
    --card-white: #ffffff;
    --brand-red: #dc4656;
    --brand-red-deep: #c3202f;
    --brand-blue: #2f5aa0;
    --text-light: #ffffff;
    --shadow: rgba(0, 0, 0, 0.18);
  }
  * { box-sizing: border-box; margin: 0; padding: 0; }
  html, body { width: 1200px; height: 913px; overflow: hidden; }
  body {
    background: var(--page-bg);
    font-family: "Open Sans", Arial, sans-serif;
    position: relative;
  }
  .card {
    position: absolute;
    left: 285px;
    width: 630px;
    height: 360px;
    background: var(--card-white);
    box-shadow: 0 6px 18px var(--shadow);
    overflow: hidden;
  }
  .card--front { top: 62px; }
  .card--back { top: 490px; }

  .card__wave { position: absolute; inset: 0; width: 100%; height: 100%; }

  .brand-name {
    position: absolute;
    color: var(--brand-blue);
    font-weight: 800;
    text-transform: uppercase;
    line-height: 1.05;
    text-align: center;
    display: flex;
    align-items: center;
    gap: 12px;
  }
  .brand-name__dot {
    width: 18px; height: 18px;
    border-radius: 50%;
    background: var(--brand-red);
    flex: none;
  }
  .card--front .brand-name {
    left: 30px; top: 128px; width: 230px;
    font-size: 26px;
    justify-content: center;
  }
  .card--back .brand-name {
    left: 50%; top: 50%;
    transform: translate(-50%, -50%);
    font-size: 34px;
    width: 330px;
  }

  .contact {
    position: absolute;
    right: 34px;
    top: 96px;
    text-align: right;
    color: var(--text-light);
  }
  .contact__name { font-size: 26px; font-weight: 700; line-height: 1.1; }
  .contact__role { font-size: 13px; margin-bottom: 16px; }
  .contact__line {
    font-size: 13px;
    line-height: 1.75;
    display: flex;
    justify-content: flex-end;
    align-items: center;
    gap: 8px;
  }
  .contact__icon { width: 12px; height: 12px; flex: none; }
</style>
</head>
<body>

<section class="card card--front">
  <svg class="card__wave" viewBox="0 0 630 360" preserveAspectRatio="none" aria-hidden="true">
    <defs>
      <linearGradient id="redPanel" x1="0" y1="0" x2="0" y2="1">
        <stop offset="0" stop-color="var(--brand-red)"/>
        <stop offset="1" stop-color="var(--brand-red-deep)"/>
      </linearGradient>
    </defs>
    <path d="M495 0 C410 0 370 120 305 220 C245 315 130 358 0 360 L630 360 L630 0 Z" fill="url(#redPanel)"/>
    <path d="M495 0 C410 0 370 120 305 220 C245 315 130 358 0 360" fill="none" stroke="var(--brand-blue)" stroke-width="6"/>
    <path d="M503 4 C420 4 380 124 313 224 C253 319 138 362 0 364" fill="none" stroke="#ffffff" stroke-width="1.5" opacity="0.9"/>
  </svg>

  <div class="brand-name"><span>Coastline Motor Traders</span></div>

  <div class="contact">
    <p class="contact__name">Martin Kelloway</p>
    <p class="contact__role">Owner</p>
    <p class="contact__line">+61417 562 304
      <svg class="contact__icon" viewBox="0 0 12 12" aria-hidden="true"><rect x="3" y="0.5" width="6" height="11" rx="1.2" fill="none" stroke="#fff"/><circle cx="6" cy="9.5" r="0.7" fill="#fff"/></svg>
    </p>
    <p class="contact__line">martin kelloway@mailbox-example.com
      <svg class="contact__icon" viewBox="0 0 12 12" aria-hidden="true"><rect x="0.5" y="2.5" width="11" height="7" fill="none" stroke="#fff"/><path d="M0.5 2.5 L6 6.5 L11.5 2.5" fill="none" stroke="#fff"/></svg>
    </p>
    <p class="contact__line">Port Ellery, QLD Australia
      <svg class="contact__icon" viewBox="0 0 12 12" aria-hidden="true"><path d="M6 11.5 C3 7.5 2 6 2 4.2 A4 4 0 0 1 10 4.2 C10 6 9 7.5 6 11.5 Z" fill="#fff"/><circle cx="6" cy="4.3" r="1.4" fill="var(--brand-red)"/></svg>
    </p>
  </div>
</section>

<section class="card card--back">
  <div class="brand-name"><span class="brand-name__dot"></span><span>Coastline Motor Traders</span></div>
</section>

</body>
</html>
```